Graphic Design for Labels

I'm needing a label for my skincare line based in Vancouver, BC. The name of the company is 'Linden Mist Skincare' and the tag line is 'Stay Gentle with Your Face'. It should indicate somewhere on the lable that it is made with raw fireweed honey.
There are two products the first is Moisturizing Face Cream and second is Nourishing Face Buff. I would like some honey-comb incorporated around the edges of the label and a black and white detailed honeybee somewhere on the label, maybe looking like it was hand drawn with a fine tip black marker or pencil. It will need to have the amount of product in the front which is 120 ml.
I'm open to different colours but nothing too bright, I want a delicate feel to the colours. Overall I would like the label to have a boutiquey artisan feel. I will also require an ingredient label for the back of the bottles the exact same size as the front label with the company info there as well. And some directions. The ingredients and directions can read whatever for now and I will provide those details when I'm ready to order the labels if that's possible, if not let me know asap and I can provide the details. After the ingredients list I would like it to read:
'Paraben and Sulfate free'
At the bottom of the back label I would like it to read:
'Please Recycle'
and then the company name and location at the very bottom
Updates
I like the way this label is organized, and especially how the company name is in the circle around the butterfly. Maybe that could be done with a honey bee and if the Net Weight could be included like it is on this bottle that would be great - 4 oz (115g)
The flowers are nice, but maybe it would look good to have simlpe hand drawn flowers with a bee flying around, if possible?
Target Market(s)
Women
Industry/Entity Type
Graphic Design
Look and feel
Each slider illustrates characteristics of the customer's brand and the style your logo design should communicate.

```html
<!DOCTYPE html>
<html lang="en">
<head>
<meta charset="utf-8">
<title>Linden Mist Skincare – Label Options</title>
<link href="https://fonts.googleapis.com/css2?family=Tenor+Sans&family=Raleway:wght@500&family=Caveat+Brush&family=Exo+2:wght@400&display=swap" rel="stylesheet">
<style>
  :root {
    --page-white: #ffffff;
    --page-tan: #dcaa88;
    --peach-edge: #d7a487;
    --peach-centre: #f7ece6;
    --mint-edge: #bfe2d2;
    --mint-centre: #f6fbf8;
    --brown-dark: #6b3a1f;
    --brown-text: #5a3018;
    --copper: #c98a62;
    --frame: #4a3a30;
    --comb-deep: rgba(184, 128, 58, 0.85);
    --comb-mid: rgba(236, 200, 140, 0.6);
  }
  * { box-sizing: border-box; margin: 0; padding: 0; }
  html, body { width: 1044px; height: 1200px; overflow: hidden; }
  body {
    position: relative;
    background: linear-gradient(90deg, var(--page-white) 0, var(--page-white) 340px, var(--page-tan) 740px, var(--page-tan) 100%);
    font-family: "Raleway", sans-serif;
  }
  .label {
    position: absolute;
    width: 384px;
    height: 470px;
    overflow: hidden;
    text-align: center;
    color: var(--brown-text);
  }
  .label--peach { background: radial-gradient(ellipse 70% 60% at 55% 45%, var(--peach-centre) 0, #edd3c4 55%, var(--peach-edge) 100%); }
  .label--mint  { background: radial-gradient(ellipse 70% 60% at 55% 40%, var(--mint-centre) 0, #dcf0e6 55%, var(--mint-edge) 100%); }
  .label--soft  { box-shadow: inset 0 0 22px 14px var(--page-white); }
  .label--framed { border: 1.5px solid var(--frame); }

  .label__honeycomb {
    position: absolute;
    left: 0; top: 160px;
    width: 100%; height: 310px;
    background:
      radial-gradient(ellipse 45% 55% at 8% 55%, var(--comb-deep), transparent 80%),
      radial-gradient(ellipse 30% 30% at 85% 88%, rgba(210,160,90,.6), transparent 80%),
      radial-gradient(ellipse 60% 60% at 30% 70%, var(--comb-mid), transparent 85%);
  }
  .label__mark {
    position: absolute; left: 50%; top: 24px;
    width: 84px; height: 84px; margin-left: -42px;
    border: 4px solid var(--copper);
    border-radius: 50%;
  }
  .label__brand {
    position: absolute; left: 0; right: 0; top: 104px;
    font-family: "Tenor Sans", sans-serif;
    font-size: 31px; line-height: 36px;
    color: var(--copper);
  }
  .label__brand-sub {
    display: block;
    font-size: 11px; line-height: 12px;
    letter-spacing: 4px;
  }
  .label__rule {
    position: absolute; left: 70px; right: 62px; top: 157px;
    border-top: 1.5px solid var(--copper);
  }
  .label__type {
    position: absolute; left: 0; right: 0; top: 206px;
    font-size: 22px; letter-spacing: 1px;
    color: var(--brown-text);
  }
  .label__product {
    position: absolute; left: 0; right: 0; top: 236px;
    font-family: "Caveat Brush", cursive;
    font-size: 64px; line-height: 1;
    color: var(--brown-dark);
  }
  .label__tagline {
    position: absolute; left: 0; right: 0; top: 366px;
    font-family: "Exo 2", sans-serif;
    font-size: 30px; line-height: 42px;
    color: var(--brown-dark);
  }
</style>
</head>
<body>

  <section class="label label--peach label--soft" style="left:100px; top:137px;">
    <div class="label__honeycomb" role="img" aria-label="Golden honeycomb cells along the lower left edge with curled flourishes"></div>
    <div class="label__mark"></div>
    <div class="label__brand">Linden Mist<span class="label__brand-sub">Skincare</span></div>
    <div class="label__rule"></div>
    <div class="label__type">Moisturizing</div>
    <div class="label__product">Face Cream</div>
    <div class="label__tagline">Stay Gentle<br>with Your Face</div>
  </section>

  <section class="label label--peach label--framed" style="left:551px; top:136px; height:472px; width:388px;">
    <div class="label__honeycomb" role="img" aria-label="Golden honeycomb cells along the lower left edge with curled flourishes"></div>
    <div class="label__mark"></div>
    <div class="label__brand">Linden Mist<span class="label__brand-sub">Skincare</span></div>
    <div class="label__rule"></div>
    <div class="label__type">Moisturizing</div>
    <div class="label__product">Face Cream</div>
    <div class="label__tagline">Stay Gentle<br>with Your Face</div>
  </section>

  <section class="label label--mint label--soft" style="left:108px; top:636px; width:375px; height:467px;">
    <div class="label__honeycomb" role="img" aria-label="Golden honeycomb cells along the lower left edge with curled flourishes"></div>
    <div class="label__mark"></div>
    <div class="label__brand">Linden Mist<span class="label__brand-sub">Skincare</span></div>
    <div class="label__rule"></div>
    <div class="label__type">Nourishing</div>
    <div class="label__product">Face Buff</div>
    <div class="label__tagline">Stay Gentle<br>with Your Face</div>
  </section>

  <section class="label label--mint label--framed" style="left:552px; top:645px; width:386px; height:468px;">
    <div class="label__honeycomb" role="img" aria-label="Golden honeycomb cells along the lower left edge with curled flourishes"></div>
    <div class="label__mark"></div>
    <div class="label__brand">Linden Mist<span class="label__brand-sub">Skincare</span></div>
    <div class="label__rule"></div>
    <div class="label__type">Nourishing</div>
    <div class="label__product">Face Buff</div>
    <div class="label__tagline">Stay Gentle<br>with Your Face</div>
  </section>

</body>
</html>
```